Need a new design for Glass Cleaner label. The brand name already exists i.e. VOSTA. Tarn is the company name. Looking for new design. It's application is for cleaning glasses in houses, cars, offices e.t.c. Our product gives streak free shine and anti static effect. Images of old label design is attached. Bottle will be same as before. It's better to show a car as well in the design but not necessary. New logo's of vosta can also be designed.

Household and automobile

It Company

```html
<!DOCTYPE html>
<html lang="en">
<head>
<meta charset="utf-8">
<title>Tarn VOSTA Glass Cleaner Label</title>
<link href="https://fonts.googleapis.com/css2?family=Fira+Sans+Condensed:wght@400;600;700;900&display=swap" rel="stylesheet">
<style>
  :root {
    --stage-light: #ffffff;
    --stage-dark: #cfcfd1;
    --brand-red: #d2102e;
    --brand-red-dark: #a70a20;
    --ink-blue: #2c5aa6;
    --sky-top: #a9b8dd;
    --sky-mid: #cfe6f1;
    --sky-low: #bfe4e6;
    --icon-lilac: #9f9bd0;
    --white: #ffffff;
  }
  * { margin: 0; padding: 0; box-sizing: border-box; }
  html, body { width: 1200px; height: 1187px; overflow: hidden; }
  body {
    background: radial-gradient(ellipse at 50% 50%, var(--stage-light) 45%, var(--stage-dark) 100%);
    font-family: "Fira Sans Condensed", sans-serif;
    position: relative;
  }
  .label-frame {
    position: absolute; inset: 0;
    filter: drop-shadow(0 0 3px rgba(0,0,0,0.25));
  }
  .label {
    position: absolute; inset: 0;
    clip-path: path('M 316 352 Q 318 316 352 303 L 748 126 Q 790 110 798 150 L 862 640 L 900 960 Q 906 1012 860 1014 L 350 1016 Q 316 1016 316 985 Z');
    background:
      radial-gradient(circle at 46% 30%, rgba(255,255,255,0.85) 0, rgba(255,255,255,0) 18%),
      linear-gradient(170deg, var(--sky-top) 0%, var(--sky-mid) 45%, var(--sky-low) 100%);
  }
  .company-name {
    position: absolute; left: 596px; top: 200px;
    font-weight: 900; font-size: 80px; color: var(--brand-red);
    line-height: 1; transform: rotate(-8deg);
  }
  .claim {
    position: absolute; left: 400px; top: 282px;
    color: var(--ink-blue); font-weight: 700; text-align: center;
    line-height: 1.05; transform: rotate(-8deg);
  }
  .claim .small { font-size: 20px; display: block; }
  .claim .big { font-size: 30px; letter-spacing: 2px; display: block; }
  .claim .mid { font-size: 24px; display: block; }
  .product-name {
    position: absolute; left: 350px; top: 380px;
    font-weight: 900; font-size: 214px; line-height: 1;
    color: var(--brand-red); letter-spacing: -4px;
    transform: rotate(-6deg) scaleX(0.8); transform-origin: left bottom;
    white-space: nowrap;
  }
  .triple-action {
    position: absolute; left: 351px; top: 660px;
    color: var(--ink-blue); font-size: 38px; font-weight: 600; line-height: 1;
  }
  .benefits {
    position: absolute; left: 349px; top: 710px;
    color: var(--brand-red); font-size: 12px; font-weight: 700; font-style: italic;
  }
  .variant-band {
    position: absolute; left: 290px; top: 739px; width: 640px; height: 72px;
    background: linear-gradient(180deg, var(--brand-red) 0%, var(--brand-red-dark) 100%);
  }
  .variant-name {
    position: absolute; left: 356px; top: 742px;
    color: var(--white); font-size: 56px; font-weight: 400; line-height: 66px;
  }
  .art-window {
    position: absolute; left: 660px; top: 630px; width: 196px; height: 164px;
    background: linear-gradient(180deg, #4d8fd8 0%, #cfe3f5 100%);
    border: 6px solid var(--white);
  }
  .art-screen {
    position: absolute; left: 532px; top: 752px; width: 146px; height: 103px;
    background: linear-gradient(135deg, #3a5fae 0%, #1b2340 100%);
    border: 5px solid #1a1a1a;
  }
  .art-car {
    position: absolute; left: 648px; top: 782px; width: 232px; height: 136px;
    border-radius: 40px 40px 24px 24px;
    background: linear-gradient(180deg, #4a3f5c 0%, #1e1a28 100%);
  }
  .use-icons { position: absolute; inset: 0; }
  .usage {
    position: absolute; left: 560px; top: 946px; width: 340px;
    color: var(--ink-blue); font-size: 17px; font-weight: 700;
    text-align: center; line-height: 1.3;
  }
  .volume {
    position: absolute; left: 354px; top: 972px;
    color: var(--white); font-size: 26px; font-weight: 400;
  }
</style>
</head>
<body>
  <div class="label-frame">
    <div class="label">
      <div class="company-name">Tarn</div>
      <div class="claim">
        <span class="small">Outstanding</span>
        <span class="big">STREAK</span>
        <span class="mid">FREE Shine</span>
      </div>
      <div class="product-name">VOSTA</div>

      <div class="triple-action">triple action</div>
      <div class="benefits">✔anti-static ✔anti-dust ✔anti-streak</div>

      <div class="variant-band"></div>
      <div class="variant-name">Glass</div>

      <div class="art-window" role="img" aria-label="Open window with blue sky and clouds"></div>
      <div class="art-screen" role="img" aria-label="Flat screen television"></div>
      <div class="art-car" role="img" aria-label="Dark purple SUV"></div>

      <svg class="use-icons" width="1200" height="1187" viewBox="0 0 1200 1187" aria-label="Use areas: home, office, glasses, car">
        <g fill="var(--icon-lilac)" stroke="var(--white)" stroke-width="3">
          <circle cx="376" cy="849" r="28"/>
          <circle cx="419" cy="898" r="28"/>
          <circle cx="480" cy="938" r="28"/>
          <circle cx="535" cy="973" r="28"/>
        </g>
        <g fill="var(--white)">
          <path d="M360 850 L376 834 L392 850 L388 850 L388 864 L364 864 L364 850 Z"/>
          <rect x="404" y="892" width="26" height="4"/>
          <rect x="406" y="896" width="4" height="14"/>
          <rect x="422" y="896" width="6" height="14"/>
          <rect x="410" y="880" width="10" height="10"/>
          <path d="M462 932 L498 932 L496 942 Q492 948 484 946 L480 938 L476 946 Q468 948 464 942 Z"/>
          <path d="M518 978 L520 968 Q522 962 528 962 L542 962 Q548 962 550 968 L552 978 Z"/>
          <rect x="516" y="974" width="38" height="8" rx="3"/>
        </g>
      </svg>

      <div class="usage">Suitable for<br>home, office, car and all glass surfaces.</div>
      <div class="volume">500ml</div>
    </div>
  </div>
</body>
</html>
```